Website design in Wordpress for Golf Simulator Center

We are opening a new golf simulator center in Copenhagen, and need a website design. We are using wordpress, and our site is https://vornlo-tee.dk
We will need a design for the frontpage, and a design for subpages (which we will be reusing for all subpages).
Logo is as seen on the site, and our base color scheme is leaf green.
As text, take the text on the current website, or put some placeholder text in english.
Should be responsive and look good on both desktop and mobile.
Target Market(s)
Male, 18-60, golf players

```html
<!DOCTYPE html>
<html lang="en">
<head>
<meta charset="utf-8">
<title>Vornlo Tee – Golf Simulator in Valby</title>
<link href="https://fonts.googleapis.com/css2?family=Poppins:wght@400;500;600;700;800&display=swap" rel="stylesheet">
<style>
:root{
  --green:#0a7a0a;
  --green-dark:#056005;
  --ink:#3a3a3a;
  --text:#4a4a4a;
  --grey-band:#ebebeb;
  --footer:#434343;
  --white:#ffffff;
}
*{margin:0;padding:0;box-sizing:border-box}
html,body{width:1200px;height:3905px;overflow:hidden}
body{font-family:'Poppins',sans-serif;color:var(--text);background:var(--white);position:relative}
.abs{position:absolute}
.btn{position:absolute;display:flex;align-items:center;justify-content:center;background:var(--green);color:var(--white);font-weight:700;font-size:14px;border-radius:30px;text-decoration:none;text-transform:uppercase}
/* header */
.site-header{left:0;top:0;width:1200px;height:78px;background:var(--white)}
.brand{position:absolute;display:flex;align-items:center;gap:10px;font-weight:700;color:var(--green);letter-spacing:1px}
.brand .mark{background:var(--green)}
.site-header .brand{left:88px;top:22px;font-size:26px}
.site-header .brand .mark{width:30px;height:30px}
.main-nav{position:absolute;right:103px;top:28px;display:flex;gap:36px;font-size:14px;font-weight:700;color:#222}
/* hero */
.hero{left:0;top:78px;width:1200px;height:727px;background:radial-gradient(ellipse at 60% 25%,#3c6a4a 0%,#1e2a22 40%,#141616 70%),#141616}
.hero-floor{left:0;top:0;width:1200px;height:727px;background:linear-gradient(180deg,rgba(20,22,22,0) 0%,rgba(20,22,22,0) 60%,rgba(36,84,36,.55) 85%,rgba(22,40,22,.7) 100%)}
.hero h1{position:absolute;left:0;width:1200px;top:215px;text-align:center;color:var(--white);font-size:66px;line-height:66px;font-weight:800}
.hero p{position:absolute;left:0;width:1200px;top:363px;text-align:center;color:var(--white);font-size:15px;line-height:23px}
.hero .btn{left:513px;top:435px;width:174px;height:56px}
/* features */
.photo{position:absolute}
h2.feature-title{position:absolute;color:var(--ink);font-size:31px;line-height:31px;font-weight:700;text-transform:uppercase}
.feature-text{position:absolute;font-size:15px;line-height:21.5px}
/* blog */
.blog-band{left:0;top:2560px;width:1200px;height:390px;background:var(--grey-band)}
.blog-heading{left:0;width:1200px;top:2640px;text-align:center;font-size:31px;font-weight:700;color:var(--ink)}
.post{position:absolute;width:499px}
.post .photo{position:relative;width:499px;height:380px}
.post .date{margin-top:22px;font-size:15px;font-weight:700;color:var(--green)}
.post h3{margin-top:6px;font-size:15px;font-weight:700;color:#222}
.post p{margin-top:10px;width:482px;font-size:14.5px;line-height:20px}
/* newsletter + footer */
.footer-bg{left:0;top:3418px;width:1200px;height:487px;background:var(--footer)}
.newsletter{left:148px;top:3322px;width:879px;height:190px;background:linear-gradient(120deg,#087908,#0b8a0b 60%,#076d07)}
.newsletter h2{position:absolute;left:48px;top:64px;font-size:30px;line-height:32px;font-weight:800;color:var(--white)}
.newsletter .field{position:absolute;left:393px;top:70px;width:314px;height:51px;background:var(--white);border-radius:26px 0 0 26px;font-size:14px;color:#555;padding:15px 25px}
.newsletter .subscribe{position:absolute;left:707px;top:70px;width:138px;height:51px;background:var(--footer);border-radius:0 26px 26px 0;color:var(--white);font-weight:700;font-size:14px;display:flex;align-items:center;justify-content:center}
.site-footer .brand{left:110px;top:3658px;font-size:38px;color:var(--white)}
.site-footer .brand .mark{width:42px;height:42px;background:var(--white)}
.foot-col{position:absolute;top:3602px;color:var(--white);font-size:13px;line-height:17px}
.foot-col h4{font-size:14.5px;font-weight:700;margin-bottom:14px}
.foot-col li{list-style:none;margin-bottom:14px}
.socials{left:867px;top:3668px;display:flex;gap:12px}
.socials span{width:34px;height:34px;border-radius:50%;background:#8c8c8c}
.foot-rule{left:88px;top:3846px;width:1024px;height:1px;background:#666}
.copyright{left:0;width:1200px;top:3868px;text-align:center;color:var(--white);font-size:13px}
</style>
</head>
<body>

<header class="abs site-header">
  <div class="brand"><span>VORNLO</span><span class="mark"></span><span>TEE</span></div>
  <nav class="main-nav"><span>GOLF SMIULATOR</span><span>RESOURCES</span><span>ABOUT US</span></nav>
</header>

<section class="abs hero">
  <div class="abs hero-floor" role="img" aria-label="Golfer swinging on a green hitting mat in front of a simulator screen showing a seaside course"></div>
  <h1>GOLF SIMULATOR<br>IN VALBY</h1>
  <p>Indoor golf center with 8 simulators in Valby. Play golf indoors in all weathers,<br>whether driving range or a full 18-hole round.</p>
  <a class="btn">See more</a>
</section>

<div class="photo" style="left:124px;top:894px;width:574px;height:556px;background:linear-gradient(160deg,#d8dad4 0%,#9fb09a 45%,#4d7a3c 75%,#5a4a48 100%)" role="img" aria-label="Simulator lounge with armchairs facing a large course screen"></div>
<h2 class="feature-title" style="left:762px;top:958px">Golf simulator<br>in Valby opens<br>January 2023</h2>
<p class="feature-text" style="left:762px;top:1062px;width:330px">In January 2023, a new golf simulator center will open in Valby with 8 simulators of the Fairvex 4 type. We look forward to being able to welcome new and experi­enced golfers. With us, you can practice all kinds of shots indoors, sheltered from rain and snow, or play an entire 18-hole course in half the time.</p>
<a class="btn" style="left:762px;top:1257px;width:174px;height:56px">See more</a>

<div class="photo" style="left:537px;top:1412px;width:574px;height:556px;background:linear-gradient(180deg,#d6dcd8 0%,#6c8a5a 40%,#3f6a2e 75%,#223a1e 100%)" role="img" aria-label="Golfer hitting a shot in a simulator bay with a tree-lined fairway on screen"></div>
<h2 class="feature-title" style="left:88px;top:1622px">Opening reception</h2>
<p class="feature-text" style="left:88px;top:1664px;width:362px;line-height:22px">We will hold an opening reception on 20 Janu­ary 2023 from 4 p.m. More information will be available on this page continuously, and via our newsletter, which you can sign up for here. We also give a discount code for 1 hour of free play to everyone who signs up for our newsletter before the New Year and who is still signed up for the newsletter at our opening reception.</p>

<div class="photo" style="left:168px;top:1994px;width:690px;height:566px;background:radial-gradient(ellipse at 40% 55%,#c8e03a 0%,#a6c52a 45%,#ffffff 80%)" role="img" aria-label="Golfer in a lime polo shirt at the top of his backswing"></div>
<h2 class="feature-title" style="left:610px;top:2188px">Buy a starter<br>membership right<br>now!</h2>
<p class="abs" style="left:610px;top:2301px;font-size:14.5px;font-weight:700;color:#333">FOR YOURSELF OR AS A GIFT - MORE INFORMATION</p>
<a class="btn" style="left:612px;top:2341px;width:226px;height:57px">Starter membership</a>

<div class="abs blog-band"></div>
<h2 class="abs blog-heading">LATEST BLOG</h2>
<article class="post" style="left:96px;top:2700px">
  <div class="photo" role="img" aria-label="Golfer driving a ball in a simulator bay with a bag of clubs beside him" style="background:linear-gradient(180deg,#7fb05a 0%,#4e8a34 50%,#2f5a24 100%)"></div>
  <div class="date">10-01-2023</div>
  <h3>THE FIRST BLOW HAS BEEN STRUCK!</h3>
  <p>The first blow on the first simulator has been struck, and now we just need to have the other 7 completed. The picture is actually from the second battle...</p>
</article>
<article class="post" style="left:607px;top:2700px">
  <div class="photo" role="img" aria-label="Golf pro coaching a player on a simulator mat" style="background:linear-gradient(180deg,#c8d8cc 0%,#4f8a3c 45%,#2c5a22 100%)"></div>
  <div class="date">10-01-2023</div>
  <h3>GOLF TRAINING ON A SIMULATOR</h3>
  <p>Golf training can be done directly on a golf simulator at Vornlo Tee in Valby. Here you get the opportunity to train with a Pro, or train yourself...</p>
</article>

<div class="abs footer-bg"></div>
<section class="abs newsletter">
  <h2>SIGN UP FOR OUR<br>NEWSLETTER!</h2>
  <div class="field">Enter your email address....</div>
  <div class="subscribe">SUBSCRIBE</div>
</section>

<footer class="site-footer">
  <div class="brand"><span>VORNLO</span><span class="mark"></span><span>TEE</span></div>
  <div class="foot-col" style="left:452px">
    <h4>QUICK LINKS</h4>
    <ul><li>Home</li><li>Golf smiulator</li><li>Resources</li><li>About us</li></ul>
  </div>
  <div class="foot-col" style="left:632px">
    <h4>VORNLO TEE APS</h4>
    <p>Kranvej 14<br>2500 Valby<br>CVR: 40918236<br>Tel: 31 47 62 05<br>Open 15:00-22:00 Mon-Sun</p>
  </div>
  <div class="abs socials"><span></span><span></span><span></span><span></span><span></span></div>
  <div class="abs foot-rule"></div>
  <p class="abs copyright">©Copyright 2023 | All Rights Reserved</p>
</footer>

</body>
</html>
```